Hadley's Groundwork Crew needs a logo/business cards.

i've just started a new Labouring Business, Called Hadley's Groundwork Crew, I provide high quality labouring servicing to local Builders and Tradesmen.
I'd like my business cards to reflect the hard work and dedication I put into my business.
I'd like to see Burnt Orange and blacks in the cards and logo.
I want my cards to catch peoples eye as there is A lot of dull business cards in my industry.

Target Market(s)

Builders and other tradesmen

Contact Information for Business Card

Hadley's Groundwork Crew

Font styles to use
Sans Serif

Colors
f78f20
ffc214
000000
ffffff

Requirements
Must have
• My name : Tom Hadley
• My Number: 0457962381
• Email Address : hadleygroundworkcrew@mailbarn.net
• A Sharp and Professional Design
Nice to have
• A unique design that separates my Cards from others,
• As I try to provide unique service to my clients I'd love my cards/logo to reflect this.

```html
<!DOCTYPE html>
<html lang="en">
<head>
<meta charset="utf-8">
<title>Hadley's Groundwork Crew — Business Card</title>
<link rel="stylesheet" href="https://fonts.googleapis.com/css2?family=Work+Sans:wght@400;500;600&display=swap">
<style>
  :root {
    --bg: #161616;
    --card: #232323;
    --orange: #f78f20;
    --white: #ffffff;
    --logo-grey: #8a8a8a;
  }
  * { margin: 0; padding: 0; box-sizing: border-box; }
  html, body {
    width: 1200px; height: 900px; overflow: hidden;
    background: radial-gradient(ellipse at 60% 40%, #262626 0%, var(--bg) 75%);
    font-family: "Work Sans", sans-serif;
  }
  .sheet {
    position: relative; width: 1200px; height: 900px;
    display: flex; flex-direction: column; align-items: center; justify-content: center; gap: 44px;
  }
  .card {
    position: relative; width: 680px; height: 388px;
    background: var(--card);
    box-shadow: 0 14px 30px rgba(0,0,0,0.55);
  }
  .card--front { display: flex; align-items: center; justify-content: center; }
  .brand-name {
    color: var(--logo-grey); font-weight: 600; font-size: 34px;
    letter-spacing: 0.06em; text-transform: uppercase; text-align: center; line-height: 1.2;
  }
  .brand-name span { display: block; }
  .card--back { display: flex; align-items: center; justify-content: center; padding: 0 30px; }
  .person { text-align: right; flex: none; }
  .person__name {
    color: var(--orange); font-weight: 500; font-size: 30px;
    text-transform: uppercase; letter-spacing: 0.02em; line-height: 1; white-space: nowrap;
  }
  .person__role { color: var(--white); font-size: 17px; margin-top: 6px; letter-spacing: 0.03em; }
  .divider { flex: none; width: 2px; height: 112px; background: var(--orange); margin: 0 24px; }
  .contact { color: var(--white); font-size: 15px; line-height: 1.4; letter-spacing: 0.03em; white-space: nowrap; }
  .contact__address { margin-bottom: 4px; }
  .contact__row { display: flex; align-items: center; gap: 8px; }
  .contact__icon { width: 12px; height: 12px; flex: none; }
</style>
</head>
<body>
<main class="sheet">
  <section class="card card--front">
    <h1 class="brand-name"><span>Hadley's</span><span>Groundwork Crew</span></h1>
  </section>

  <section class="card card--back">
    <div class="person">
      <p class="person__name">Tom Hadley</p>
      <p class="person__role">Director</p>
    </div>
    <div class="divider"></div>
    <div class="contact">
      <p class="contact__address">2719 Marlow Lane<br>Brookvale, TX 78410</p>
      <p class="contact__row">
        <svg class="contact__icon" viewBox="0 0 16 16" aria-hidden="true"><path d="M4 1 L6.5 4.5 L5 6.5 Q6.5 9.5 9.5 11 L11.5 9.5 L15 12 L13 15 Q5 14 1 3 Z" fill="var(--orange)"/></svg>
        0457 962 381
      </p>
      <p class="contact__row">
        <svg class="contact__icon" viewBox="0 0 16 16" aria-hidden="true"><rect x="1" y="3" width="14" height="10" fill="none" stroke="var(--orange)" stroke-width="1.5"/><path d="M1 3 L8 9 L15 3" fill="none" stroke="var(--orange)" stroke-width="1.5"/></svg>
        hadleygroundworkcrew@mailbarn.net
      </p>
      <p class="contact__row">
        <svg class="contact__icon" viewBox="0 0 16 16" aria-hidden="true"><circle cx="8" cy="8" r="6.5" fill="none" stroke="var(--orange)" stroke-width="1.3"/><ellipse cx="8" cy="8" rx="3" ry="6.5" fill="none" stroke="var(--orange)" stroke-width="1.1"/><path d="M1.5 8 H14.5" stroke="var(--orange)" stroke-width="1.1"/></svg>
        www.tom_hadley.net
      </p>
    </div>
  </section>
</main>
</body>
</html>
```